Real estate website

Please find attached a rough outline of what we want for the design. This is just for placement to show what to have on the menu's as content, etc. but please make it look much more professional.
Please make the bottom footer a similar gradient to the logo
Please make the sign up now and log in buttons look better - these are just samples to show placement
Please use the correct logos for brindlequay.com.au, tovrel.com.au and quintaro.com.au
Where it has 'video embed' just leave that as is as we will replace that with a video.

```html
<!DOCTYPE html>
<html lang="en">
<head>
<meta charset="utf-8">
<title>Keyvale Homes – Sell with no commission</title>
<link rel="stylesheet" href="https://fonts.googleapis.com/css2?family=Roboto:wght@300;400;500;700&display=swap">
<style>
:root{
  --green-dark:#0e6b35;
  --green-mid:#1d7a3c;
  --green-light:#8cc63f;
  --panel:#1f6e3c;
  --ink:#222;
  --muted:#555;
  --placeholder:#555;
  --white:#fff;
}
*{box-sizing:border-box;margin:0;padding:0}
html,body{width:1200px;height:675px;overflow:hidden}
body{font-family:'Roboto',sans-serif;position:relative;background:#f6f6f6;color:var(--ink)}
.site-header{position:absolute;left:0;top:0;width:1200px;height:99px;background:#f7f7f7;border-bottom:1px solid #555}
.brand{position:absolute;left:39px;top:15px;height:63px;display:flex;align-items:center;gap:14px}
.brand-mark{width:34px;height:34px;border-radius:50%;background:var(--green-dark)}
.brand-name{font-size:30px;font-weight:300;color:#222;letter-spacing:.3px}
.main-nav{position:absolute;top:38px;left:306px;display:flex;gap:31px;font-size:15.5px;color:#333;letter-spacing:.2px}
.btn{position:absolute;height:41.5px;border-radius:21px;color:var(--white);font-size:16px;display:flex;align-items:center;justify-content:center;gap:7px;letter-spacing:.3px}
.btn-signup{left:857px;top:27.5px;width:148px;background:var(--green-dark)}
.btn-login{left:1013px;top:27.5px;width:148px;background:var(--green-light)}
.hero{position:absolute;left:0;top:99px;width:733px;height:476px;background:linear-gradient(135deg,#fafafa 0%,#eeeeee 55%,#f4f4f4 100%)}
.hero-title{position:absolute;left:47px;top:54px;font-size:37.5px;font-weight:700;color:var(--green-dark);letter-spacing:-.2px}
.listings{position:absolute;left:47px;top:126px;list-style:none}
.listings li{display:flex;align-items:center;height:49px}
.listings .tick{width:34px;height:34px;margin-right:26px}
.listings .portal{font-size:24px;font-weight:700;color:#444}
.agent-video{position:absolute;left:47px;top:285px;width:134px;height:191px;background:linear-gradient(180deg,#d8d8d8,#3a3a3a)}
.upfront{position:absolute;left:189px;top:316px;font-size:26px;font-weight:700;color:var(--green-dark)}
.ask{position:absolute;left:189px;top:358px;font-size:20px;font-weight:500;color:#222}
.ask .phone{font-size:27.5px;color:var(--green-light);font-weight:500}
.intro{position:absolute;left:190px;top:394px;width:520px;font-size:12.5px;line-height:19px;color:var(--muted)}
.guide-panel{position:absolute;left:733px;top:99px;width:467px;height:476px;background:linear-gradient(160deg,#1f7140,#185f33 60%,#1e6c3b)}
.guide-title{position:absolute;left:0;width:100%;top:38px;text-align:center;color:var(--white);font-size:25px;font-weight:700}
.guide-sub{position:absolute;left:0;width:100%;top:78px;text-align:center;color:var(--white);font-size:16px}
.field{position:absolute;left:37px;width:392.5px;height:42.5px;border-radius:22px;background:var(--white);display:flex;align-items:center;padding-left:24px;gap:8px;font-size:12.5px;color:var(--placeholder)}
.field svg{width:13px;height:13px;fill:#666}
.submit{position:absolute;left:165px;top:341px;width:136px;height:42.5px;border-radius:22px;background:var(--green-light);color:var(--green-dark);font-weight:700;font-size:12.5px;display:flex;align-items:center;justify-content:center;letter-spacing:.2px}
.captcha{position:absolute;left:139px;top:400px;width:189px;height:47px;background:#f9f9f9;border:1px solid #d3d3d3;border-radius:2px;font-size:8.5px;color:#222}
.captcha .check{position:absolute;left:10px;top:13px;width:18px;height:18px}
.captcha .label{position:absolute;left:31px;top:19px}
.captcha .meta{position:absolute;right:7px;top:11px;text-align:right;font-size:5.5px;color:#777;line-height:9px}
.captcha .meta b{display:block;font-weight:400}
.services{position:absolute;left:0;top:575px;width:1200px;height:100px;background:linear-gradient(90deg,var(--green-dark) 0%,#3a9233 50%,var(--green-light) 100%);list-style:none}
.services li{position:absolute;top:26px;height:48px;display:flex;align-items:center;gap:11px;color:var(--white);font-size:14px;line-height:18.5px}
.services .icon{width:48px;height:48px;border-radius:50%;background:var(--white);display:flex;align-items:center;justify-content:center}
.services .icon svg{width:28px;height:28px;fill:none;stroke:var(--green-dark);stroke-width:1.6;stroke-linecap:round;stroke-linejoin:round}
</style>
</head>
<body>
<header class="site-header">
  <div class="brand"><span class="brand-mark"></span><span class="brand-name">Keyvale Homes</span></div>
  <nav class="main-nav"><span>SELL MY PROPERTY</span><span>RENT MY PROPERTY</span><span>RENTAL MANAGEMENT</span></nav>
  <a class="btn btn-signup">
    <svg width="15" height="14" viewBox="0 0 15 14" fill="none" stroke="#fff" stroke-width="1.8"><path d="M1 7h8M6 4l3 3-3 3"/><path d="M9 1h4v12H9"/></svg>SIGN UP</a>
  <a class="btn btn-login">
    <svg width="12" height="13" viewBox="0 0 12 13" fill="#fff"><circle cx="6" cy="3.5" r="3.2"/><path d="M0 13v-2.5C0 8 2 7 6 7s6 1 6 3.5V13z"/></svg>LOG IN</a>
</header>

<section class="hero" role="img" aria-label="Bright, softly faded living room interior">
  <h1 class="hero-title">Sell with no commission on</h1>
  <ul class="listings">
    <li><svg class="tick" viewBox="0 0 34 34"><circle cx="17" cy="17" r="15.5" fill="none" stroke="#6cbf4a" stroke-width="2"/><path d="M10 17.5l5 5 9-10" fill="none" stroke="#2e8b3e" stroke-width="2"/></svg><span class="portal">brindlequay.com.au</span></li>
    <li><svg class="tick" viewBox="0 0 34 34"><circle cx="17" cy="17" r="15.5" fill="none" stroke="#6cbf4a" stroke-width="2"/><path d="M10 17.5l5 5 9-10" fill="none" stroke="#2e8b3e" stroke-width="2"/></svg><span class="portal">tovrel.com.au</span></li>
    <li><svg class="tick" viewBox="0 0 34 34"><circle cx="17" cy="17" r="15.5" fill="none" stroke="#6cbf4a" stroke-width="2"/><path d="M10 17.5l5 5 9-10" fill="none" stroke="#2e8b3e" stroke-width="2"/></svg><span class="portal">quintaro.com.au</span></li>
  </ul>
  <div class="agent-video" role="img" aria-label="Video embed placeholder: presenter in a dark suit"></div>
  <h2 class="upfront">Want to Pay Nothing Upfront?</h2>
  <p class="ask">Ask us How <span class="phone">-0412558903</span></p>
  <p class="intro">Lorem ipsum dolor sit amet, consectetur adipiscing elit, sed do eiusmod tempor incididunt ut labore et dolore magna aliqua. Ut enim ad minim veniam, quis nostrud exercitation ullamco laboris nisi ut aliquip ex ea commodo consequat.</p>
</section>

<aside class="guide-panel">
  <h2 class="guide-title">GET YOUR FREE GUIDE</h2>
  <p class="guide-sub">To listing privately in the ACT</p>
  <div class="field" style="top:116px"><svg viewBox="0 0 14 14"><path d="M0 3h14v9H0z M0 3l7 5 7-5" /></svg>Email address*</div>
  <div class="field" style="top:172px"><svg viewBox="0 0 12 13"><circle cx="6" cy="3.5" r="3.2"/><path d="M0 13v-2.5C0 8 2 7 6 7s6 1 6 3.5V13z"/></svg>First name*</div>
  <div class="field" style="top:228.5px"><svg viewBox="0 0 12 13"><circle cx="6" cy="3.5" r="3.2"/><path d="M0 13v-2.5C0 8 2 7 6 7s6 1 6 3.5V13z"/></svg>Last name</div>
  <div class="field" style="top:285px"><svg viewBox="0 0 14 14"><path d="M3 0l3 3-2 2c1 2 3 4 5 5l2-2 3 3-2 3C6 14 0 8 0 2z"/></svg>Phone number</div>
  <div class="submit">SUBMIT NOW</div>
  <div class="captcha">
    <svg class="check" viewBox="0 0 18 18"><path d="M2 9l5 5 9-11" fill="none" stroke="#1e9e4a" stroke-width="2.4"/></svg>
    <span class="label">I'm not a robot</span>
    <span class="meta"><b>HumanCheck</b>Privacy - Terms</span>
  </div>
</aside>

<ul class="services">
  <li style="left:41px"><span class="icon"><svg viewBox="0 0 28 28"><circle cx="14" cy="10" r="6"/><path d="M14 7v6M12 8.5h3M12 11.5h3"/><path d="M3 21h5l4 2h8l5-4"/></svg></span>FINANCE</li>
  <li style="left:242px"><span class="icon"><svg viewBox="0 0 28 28"><circle cx="10" cy="9" r="4"/><path d="M13 12l8 8M18 17l2-2M20 19l2-2"/></svg></span>CONVEYANCING</li>
  <li style="left:442px"><span class="icon"><svg viewBox="0 0 28 28"><path d="M4 14l8-7 8 7M6 12v10h10"/><circle cx="19" cy="16" r="4"/><path d="M22 19l3 3"/></svg></span>BUILDING<br>INSPECTION</li>
  <li style="left:642px"><span class="icon"><svg viewBox="0 0 28 28"><circle cx="14" cy="14" r="11"/><ellipse cx="14" cy="15" rx="4" ry="5"/><path d="M14 3v4M14 21v4M3 14h4M21 14h4"/></svg></span>PEST<br>INSPECTION</li>
  <li style="left:843px"><span class="icon"><svg viewBox="0 0 28 28"><path d="M6 24V10l8-6 8 6v14z"/><circle cx="14" cy="15" r="3.5"/><path d="M16.5 17.5l3 3"/></svg></span>VALUATION</li>
  <li style="left:1043px"><span class="icon"><svg viewBox="0 0 28 28"><path d="M3 14l11-9 11 9M7 11v13h14V11"/><circle cx="14" cy="16" r="3.5"/><path d="M16.5 18.5l3 3"/></svg></span>MARKET<br>APPRAISAL</li>
</ul>
</body>
</html>
```